Redesign my business cards

I would like pretty much all the same information as my current business cards but redesigned to stand out more and be more unique photo uploaded to show my current business cards don’t mind if you want to remove or replace I for on the back

```html
<!DOCTYPE html>
<html lang="en">
<head>
<meta charset="utf-8">
<title>Tidewell Detailing – Business Card</title>
<link rel="stylesheet" href="https://fonts.googleapis.com/css2?family=Montserrat:wght@500;700;800&family=Roboto:wght@400;500&display=swap">
<style>
  :root {
    --page: #ffffff;
    --card-light: #eef1f2;
    --navy: #032a3a;
    --navy-deep: #021c27;
    --aqua: #3cc4e8;
    --aqua-soft: rgba(60, 196, 232, 0.14);
    --white: #ffffff;
    --muted: #c9dde4;
  }
  * { margin: 0; padding: 0; box-sizing: border-box; }
  html, body { width: 1200px; height: 1200px; overflow: hidden; background: var(--page); }
  .canvas { position: relative; width: 1200px; height: 1200px; }

  .card { position: absolute; left: 223px; width: 764px; height: 436px; overflow: hidden; border-radius: 14px; }
  .card--front { top: 119px; background: var(--card-light); }
  .card--back { top: 645px; background: var(--navy); }

  /* Front: angled navy panel with aqua accent stripe */
  .front-stripe { position: absolute; inset: 0; background: var(--aqua); clip-path: polygon(500px 0, 764px 0, 764px 436px, 420px 436px); }
  .front-panel { position: absolute; inset: 0; background: linear-gradient(160deg, var(--navy) 0%, var(--navy-deep) 100%); clip-path: polygon(514px 0, 764px 0, 764px 436px, 434px 436px); }
  .front-base { position: absolute; left: 0; bottom: 0; width: 440px; height: 10px; background: var(--navy); }

  .owner { position: absolute; left: 40px; top: 92px; }
  .owner-name { font: 800 36px/1 "Montserrat", sans-serif; color: var(--navy); letter-spacing: 0.5px; }
  .owner-role { margin-top: 10px; font: 500 18px/1 "Montserrat", sans-serif; color: var(--navy); letter-spacing: 3px; text-transform: uppercase; }
  .owner-rule { margin-top: 16px; width: 64px; height: 4px; background: var(--aqua); border-radius: 2px; }

  .contact-list { position: absolute; left: 40px; top: 232px; list-style: none; display: flex; flex-direction: column; gap: 16px; }
  .contact { display: flex; align-items: center; gap: 12px; color: var(--navy); }
  .contact-icon { flex: none; width: 34px; height: 34px; border-radius: 50%; background: var(--navy); display: flex; align-items: center; justify-content: center; }
  .contact--phone { font: 700 20px/1 "Montserrat", sans-serif; letter-spacing: 1px; }
  .contact--email { font: 500 17px/1 "Roboto", sans-serif; letter-spacing: 0.3px; }

  .brand { position: absolute; display: flex; flex-direction: column; align-items: center; }
  .brand--front { left: 530px; top: 140px; width: 220px; gap: 16px; }
  .brand--back { right: 28px; bottom: 26px; width: 150px; gap: 8px; }
  .brand-dot { border-radius: 50%; background: var(--aqua); }
  .brand--front .brand-dot { width: 84px; height: 84px; }
  .brand--back .brand-dot { width: 46px; height: 46px; }
  .brand-name { font: 700 20px/1.2 "Montserrat", sans-serif; color: var(--white); text-align: center; letter-spacing: 3px; }
  .brand--back .brand-name { font-size: 13px; letter-spacing: 2px; }

  /* Back: service menu with price tags */
  .back-glow { position: absolute; right: -120px; top: -120px; width: 320px; height: 320px; border-radius: 50%; background: var(--aqua-soft); }
  .back-edge { position: absolute; left: 0; top: 0; bottom: 0; width: 8px; background: var(--aqua); }

  .service { position: absolute; left: 40px; right: 36px; padding-left: 16px; border-left: 3px solid var(--aqua); }
  .service-head { display: flex; justify-content: space-between; align-items: center; }
  .service-title { font: 800 22px/1 "Montserrat", sans-serif; color: var(--aqua); letter-spacing: 2px; }
  .service-price { font: 800 18px/1 "Montserrat", sans-serif; color: var(--navy); background: var(--aqua); padding: 6px 14px; border-radius: 20px; letter-spacing: 1px; }
  .service-desc { margin-top: 7px; font: 400 16.5px/1.36 "Roboto", sans-serif; color: var(--white); }
  .service--interior { top: 24px; }
  .service--exterior { top: 148px; }
  .service--full { top: 250px; }
  .service--full .service-head { width: 100%; }
  .service--full .service-desc { width: 470px; }
</style>
</head>
<body>
<div class="canvas">

  <section class="card card--front">
    <div class="front-stripe"></div>
    <div class="front-panel"></div>
    <div class="front-base"></div>

    <div class="owner">
      <h1 class="owner-name">JAKE MORROW</h1>
      <p class="owner-role">Owner/Operator</p>
      <div class="owner-rule"></div>
    </div>

    <ul class="contact-list">
      <li class="contact contact--phone">
        <span class="contact-icon"><svg width="18" height="18" viewBox="0 0 24 24" aria-hidden="true"><path fill="#3cc4e8" d="M6.6 10.8a15.1 15.1 0 0 0 6.6 6.6l2.2-2.2a1 1 0 0 1 1-.25 11.4 11.4 0 0 0 3.6.57 1 1 0 0 1 1 1V20a1 1 0 0 1-1 1A17 17 0 0 1 3 4a1 1 0 0 1 1-1h3.5a1 1 0 0 1 1 1c0 1.25.2 2.45.57 3.57a1 1 0 0 1-.25 1z"/></svg></span>
        0412555019
      </li>
      <li class="contact contact--email">
        <span class="contact-icon"><svg width="18" height="13" viewBox="0 0 28 20" aria-hidden="true"><rect width="28" height="20" rx="2" fill="#3cc4e8"/><path d="M1 1l13 10L27 1" stroke="#032a3a" stroke-width="2" fill="none"/></svg></span>
        TIDEWELLDETAILING@MAILBOX.COM
      </li>
    </ul>

    <div class="brand brand--front">
      <span class="brand-dot" aria-hidden="true"></span>
      <span class="brand-name">TIDEWELL<br>DETAILING</span>
    </div>
  </section>

  <section class="card card--back">
    <div class="back-glow"></div>
    <div class="back-edge"></div>

    <div class="service service--interior">
      <h2 class="service-head"><span class="service-title">INTERIOR DETAIL</span><span class="service-price">$150</span></h2>
      <p class="service-desc">Vacume &amp; deep clean of carpets &amp; upholstery<br>or leather treatment, interior trim clean &amp; condition.<br>Window polish and treatment, steam clean and stain removal</p>
    </div>
    <div class="service service--exterior">
      <h2 class="service-head"><span class="service-title">EXTERIOR DETAIL</span><span class="service-price">$250</span></h2>
      <p class="service-desc">Extreme wash &amp; polish. Exterior trim reviver &amp; protector<br>Window polish &amp; treatment,tyre dressing,engine bay cleaned.</p>
    </div>
    <div class="service service--full">
      <h2 class="service-head"><span class="service-title">FULL EXTREME DETAIL</span><span class="service-price">$350</span></h2>
      <p class="service-desc">Extreme wash &amp; polish,tyre dressing, engine bay cleaned<br>Vacume &amp; deep clean of carpets &amp; upholstery<br>or leather treatment.<br>Interior &amp; exterior trim reviver &amp; protector.<br>Window polish and treatment</p>
    </div>

    <div class="brand brand--back">
      <span class="brand-dot" aria-hidden="true"></span>
      <span class="brand-name">TIDEWELL<br>DETAILING</span>
    </div>
  </section>

</div>
</body>
</html>
```